Health care technology software systems

We have a solid logo. We have company colors that will need to be used as well. We just need a great business card design. We sell to health plans but want to be modern
Updates

Need extra days to review

Target Market(s)

Health technology sector selling into Health Plans

Industry/Entity Type

Health Care Technology

Contact Information for Business Card

Name, title, address, phone number, email

Requirements
Must have
• Use of Kembrata corporate colors - Uploaded w/ our logos

```html
<!DOCTYPE html>
<html lang="en">
<head>
<meta charset="utf-8">
<title>Kembrata Business Card</title>
<link href="https://fonts.googleapis.com/css2?family=Montserrat:wght@300;400;600;700&display=swap" rel="stylesheet">
<style>
  :root {
    --backdrop: #bfbfbf;
    --card-white: #ffffff;
    --brand-navy: #3560a8;
    --brand-sky: #2aa8e0;
    --brand-green: #4c9f4f;
    --text-grey: #777777;
    --title-grey: #a5a5a5;
    --wordmark-dark: #2b2b2b;
  }
  * { margin: 0; padding: 0; box-sizing: border-box; }
  html, body { width: 1200px; height: 1000px; overflow: hidden; }
  body {
    background: var(--backdrop);
    font-family: "Montserrat", sans-serif;
    position: relative;
  }
  .card {
    position: absolute;
    top: 320px;
    width: 543px;
    height: 310px;
    overflow: hidden;
    box-shadow: 0 4px 14px rgba(0,0,0,0.18);
  }
  .card-front {
    left: 41px;
    background: linear-gradient(90deg, var(--brand-navy) 0%, #2d8fd4 30%, var(--brand-sky) 55%, #3fa9a0 78%, var(--brand-green) 100%);
  }
  .front-skyline {
    position: absolute;
    right: 0; top: 0;
    width: 240px; height: 310px;
    background: linear-gradient(120deg, rgba(80,170,120,0.15) 0%, rgba(70,150,80,0.55) 60%, rgba(60,130,70,0.75) 100%);
  }
  .front-brand {
    position: absolute;
    left: 135px; top: 126px;
    display: flex; align-items: center; gap: 20px;
    color: var(--card-white);
  }
  .front-brand .brand-dot {
    width: 50px; height: 50px; border-radius: 50%;
    background: var(--card-white);
  }
  .front-brand .brand-name {
    font-weight: 300; font-size: 54px; letter-spacing: 1px;
  }
  .card-back {
    left: 609px;
    background: var(--card-white);
  }
  .back-brand {
    position: absolute;
    left: 34px; top: 38px;
    display: flex; align-items: center; gap: 12px;
  }
  .back-brand .brand-dot {
    width: 30px; height: 30px; border-radius: 50%;
    background: var(--brand-sky);
  }
  .back-brand .brand-name {
    font-weight: 400; font-size: 32px; color: var(--wordmark-dark);
    letter-spacing: 0.5px;
  }
  .person {
    position: absolute; left: 41px; top: 106px;
  }
  .person-name { font-weight: 700; font-size: 17px; color: var(--text-grey); line-height: 21px; }
  .person-title { font-weight: 300; font-size: 17px; color: var(--title-grey); line-height: 21px; }
  .contact-list {
    position: absolute; left: 41px; top: 166px;
    list-style: none;
  }
  .contact-item {
    display: flex; align-items: center; gap: 6px;
    font-weight: 600; font-size: 13px; color: var(--text-grey);
    height: 26px;
  }
  .contact-item.location { margin-top: 4px; }
  .contact-icon { width: 20px; height: 18px; flex: none; }
</style>
</head>
<body>
  <section class="card card-front">
    <div class="front-skyline" role="img" aria-label="Photo of a glass office tower seen from below against the sky"></div>
    <div class="front-brand">
      <span class="brand-dot"></span>
      <span class="brand-name">kembrata</span>
    </div>
  </section>

  <section class="card card-back">
    <div class="back-brand">
      <span class="brand-dot"></span>
      <span class="brand-name">kembrata</span>
    </div>
    <div class="person">
      <p class="person-name">Name</p>
      <p class="person-title">title</p>
    </div>
    <ul class="contact-list">
      <li class="contact-item">
        <svg class="contact-icon" viewBox="0 0 20 18"><path d="M5 2 L8 2 L9 6 L7 7.5 Q9 11 12 12.5 L13.5 10.5 L17 11.5 L17 14.5 Q16 16 14 16 Q4 14 3 4 Q3 2 5 2Z" fill="#777"/></svg>
        <span>877-555-0142</span>
      </li>
      <li class="contact-item">
        <svg class="contact-icon" viewBox="0 0 20 18"><rect x="1" y="3.5" width="18" height="11" fill="none" stroke="#777" stroke-width="1"/><path d="M1 3.5 L10 10 L19 3.5 M1 14.5 L7.5 8.5 M19 14.5 L12.5 8.5" fill="none" stroke="#777" stroke-width="1"/></svg>
        <span>info@kembrata.com</span>
      </li>
      <li class="contact-item">
        <svg class="contact-icon" viewBox="0 0 20 18"><g fill="none" stroke="#777" stroke-width="1"><circle cx="10" cy="9" r="7.5"/><ellipse cx="10" cy="9" rx="3.5" ry="7.5"/><path d="M2.5 9 H17.5 M4 5 H16 M4 13 H16"/></g></svg>
        <span>kembrata.com</span>
      </li>
      <li class="contact-item location">
        <svg class="contact-icon" viewBox="0 0 20 18"><path d="M10 17 Q4.5 10 4.5 6.5 A5.5 5.5 0 0 1 15.5 6.5 Q15.5 10 10 17Z" fill="none" stroke="#777" stroke-width="1"/><circle cx="10" cy="6.5" r="2" fill="none" stroke="#777" stroke-width="1"/></svg>
        <span>Riverton, Oregon</span>
      </li>
    </ul>
  </section>
</body>
</html>
```